Quilvo Garage Doors Business Card

I need a Business Card for my garage door business:
Quilvo Garage Doors.
please add:
logo
phone number: 855-3-QUILVO
(853-392)

email: service@quilvogaragedoors.com
website: www.quilvogaragedoors.com

The attached image is recommendation ONLY.

```html
<!DOCTYPE html>
<html lang="en">
<head>
<meta charset="utf-8">
<title>Quilvo Garage Doors – Business Card</title>
<link href="https://fonts.googleapis.com/css2?family=Lato:wght@400;700&display=swap" rel="stylesheet">
<style>
  :root {
    --backdrop: #2b2b2d;
    --card: #f7f7f7;
    --ink: #1a1a1a;
    --band: #121416;
    --teal: #4fb3bf;
    --muted: #555;
    --light: #ffffff;
  }
  * { margin: 0; padding: 0; box-sizing: border-box; }
  html, body { width: 1200px; height: 997px; overflow: hidden; }
  body {
    background: var(--backdrop);
    font-family: "Lato", sans-serif;
    position: relative;
  }
  .card {
    position: absolute;
    top: 344px;
    width: 540px;
    height: 309px;
    background: var(--card);
    border-radius: 18px;
    overflow: hidden;
  }
  .card--front { left: 40px; }
  .card--back { left: 620px; }
  .card__shapes { position: absolute; inset: 0; width: 100%; height: 100%; }

  .brand {
    position: absolute;
    display: flex;
    align-items: center;
    gap: 14px;
  }
  .brand__mark { background: var(--teal); flex: none; }
  .brand__name {
    color: var(--ink);
    font-weight: 700;
    line-height: 1.05;
  }
  .card--front .brand { top: 42px; right: 40px; }
  .card--front .brand__mark { width: 44px; height: 44px; }
  .card--front .brand__name { font-size: 20px; }
  .card--back .brand { top: 92px; left: 120px; }
  .card--back .brand__mark { width: 78px; height: 78px; }
  .card--back .brand__name { font-size: 34px; }

  .person { position: absolute; left: 40px; top: 118px; }
  .person__name { color: var(--teal); font-size: 20px; font-weight: 700; }
  .person__role { color: var(--muted); font-size: 14px; margin-top: 2px; }

  .contacts {
    position: absolute;
    left: 40px;
    top: 232px;
    list-style: none;
  }
  .contacts__item {
    display: flex;
    align-items: center;
    gap: 12px;
    color: var(--light);
    font-size: 15px;
    margin-bottom: 10px;
  }
  .contacts__item--phone { color: var(--teal); }
  .contacts__icon { width: 14px; height: 14px; flex: none; fill: #cfd3d6; }

  .tagline {
    position: absolute;
    left: 60px;
    top: 200px;
    color: var(--teal);
    font-size: 16px;
    font-weight: 700;
  }
  .website {
    position: absolute;
    right: 26px;
    bottom: 22px;
    color: var(--light);
    font-size: 15px;
    letter-spacing: 0.3px;
  }
</style>
</head>
<body>

<section class="card card--front" aria-label="Business card front">
  <svg class="card__shapes" viewBox="0 0 540 309" preserveAspectRatio="none" aria-hidden="true">
    <path d="M0,198 Q300,172 540,92 L540,106 Q300,190 0,214 Z" fill="var(--teal)"/>
    <path d="M0,220 Q300,198 540,114 L540,309 L0,309 Z" fill="var(--band)"/>
  </svg>
  <div class="brand">
    <span class="brand__mark"></span>
    <span class="brand__name">Quilvo<br>Garage Doors</span>
  </div>
  <div class="person">
    <p class="person__name">Daniel Korvath</p>
    <p class="person__role">Owner / Founder</p>
  </div>
  <ul class="contacts">
    <li class="contacts__item contacts__item--phone">
      <svg class="contacts__icon" viewBox="0 0 24 24"><path d="M6.6 10.8a15 15 0 0 0 6.6 6.6l2.2-2.2a1 1 0 0 1 1-.25 11.4 11.4 0 0 0 3.6.57 1 1 0 0 1 1 1V20a1 1 0 0 1-1 1A17 17 0 0 1 3 4a1 1 0 0 1 1-1h3.5a1 1 0 0 1 1 1c0 1.25.2 2.45.57 3.57a1 1 0 0 1-.25 1z"/></svg>
      855-3-QUILVO (853-392)
    </li>
    <li class="contacts__item">
      <svg class="contacts__icon" viewBox="0 0 24 24"><path d="M2 5h20v14H2z M4 7v.5l8 5 8-5V7z" fill-rule="evenodd"/></svg>
      service@quilvogaragedoors.com
    </li>
  </ul>
</section>

<section class="card card--back" aria-label="Business card back">
  <svg class="card__shapes" viewBox="0 0 540 309" preserveAspectRatio="none" aria-hidden="true">
    <path d="M220,309 Q380,236 540,196 L540,210 Q390,250 236,309 Z" fill="var(--teal)"/>
    <path d="M250,309 Q400,254 540,220 L540,309 Z" fill="var(--band)"/>
  </svg>
  <div class="brand">
    <span class="brand__mark"></span>
    <span class="brand__name">Quilvo<br>Garage Doors</span>
  </div>
  <p class="tagline">Call us for no obligation Free Quote &amp; Discount Coupons</p>
  <p class="website">www.quilvogaragedoors.com</p>
</section>

</body>
</html>
```